Redesign of Real Estate Agency Website

We need a redesign for our real estate agency website. Please see attached creative brief.

Target Market(s)

Refer to creative brief.

Industry/Entity Type

Real Estate

Requirements
Must have
• Refer to creative brief.

```html
<!DOCTYPE html>
<html lang="en">
<head>
<meta charset="utf-8">
<title>SIAMBAY.Net – Real Estate</title>
<link rel="stylesheet" href="https://fonts.googleapis.com/css2?family=Arimo:wght@400;700&display=swap">
<style>
  :root {
    --red: #d0021b;
    --red-dark: #b40018;
    --red-light: #e8203a;
    --panel: #e4e4eb;
    --content: #f4f4f7;
    --border: #c6c6cc;
    --footer-top: #acacb6;
    --footer-bottom: #7c7c88;
    --label: #333338;
    --white: #ffffff;
    --bg-top: #dcdce0;
    --bg-mid: #f6f6f8;
  }
  html, body {
    margin: 0;
    padding: 0;
    width: 1200px;
    height: 1200px;
    overflow: hidden;
  }
  body {
    position: relative;
    font-family: "Arimo", Arial, sans-serif;
    background: linear-gradient(180deg, var(--bg-top) 0%, var(--bg-mid) 8%, var(--bg-mid) 92%, var(--bg-top) 100%);
  }
  .page-shapes {
    position: absolute;
    left: 0;
    top: 0;
    width: 1200px;
    height: 1200px;
  }
  .text {
    position: absolute;
    margin: 0;
    line-height: 1;
    white-space: nowrap;
  }
  .brand-name {
    left: 560px;
    width: 520px;
    top: 174px;
    text-align: center;
    font-size: 72px;
    font-weight: 700;
    color: var(--red);
    letter-spacing: -1px;
  }
  .brand-tagline {
    left: 560px;
    width: 600px;
    top: 286px;
    text-align: center;
    font-size: 22px;
    font-weight: 700;
    color: var(--red);
    letter-spacing: -0.5px;
  }
  .main-nav a,
  .footer-nav a {
    position: absolute;
    font-size: 19px;
    color: var(--white);
    text-decoration: none;
    line-height: 1;
  }
  .main-nav a { top: 379px; }
  .footer-nav a { top: 1096px; }
  .search-label {
    left: 444px;
    top: 458px;
    font-size: 17px;
    font-weight: 700;
    color: var(--label);
  }
  .search-go {
    left: 960px;
    width: 60px;
    top: 457px;
    text-align: center;
    font-size: 16px;
    font-weight: 700;
    color: var(--white);
  }
  .side-menu a {
    position: absolute;
    left: 105px;
    font-size: 19px;
    color: var(--red);
    text-decoration: none;
    line-height: 1;
    white-space: pre;
  }
  .welcome-title {
    left: 463px;
    top: 585px;
    font-size: 30px;
    font-weight: 700;
    color: var(--red);
  }
</style>
</head>
<body>

<svg class="page-shapes" viewBox="0 0 800 800" aria-hidden="false">
  <defs>
    <linearGradient id="navRed" x1="0" y1="0" x2="0" y2="1">
      <stop offset="0" stop-color="var(--red-light)"/>
      <stop offset="1" stop-color="var(--red-dark)"/>
    </linearGradient>
    <linearGradient id="footerGrey" x1="0" y1="0" x2="0" y2="1">
      <stop offset="0" stop-color="var(--footer-top)"/>
      <stop offset="1" stop-color="var(--footer-bottom)"/>
    </linearGradient>
    <linearGradient id="photoTone" x1="0" y1="0" x2="0.4" y2="1">
      <stop offset="0" stop-color="#a9c9ec"/>
      <stop offset="0.45" stop-color="#d8d3c6"/>
      <stop offset="0.75" stop-color="#8f9b74"/>
      <stop offset="1" stop-color="#5f9a3a"/>
    </linearGradient>
    <radialGradient id="buttonRed" cx="0.4" cy="0.35" r="0.7">
      <stop offset="0" stop-color="var(--red-light)"/>
      <stop offset="1" stop-color="var(--red-dark)"/>
    </radialGradient>
  </defs>

  <!-- sidebar column -->
  <path class="sidebar-panel" d="M20 200 V715 Q20 742 47 742 H260 V200 Z" fill="var(--panel)"/>

  <!-- header panel -->
  <path class="header-panel" d="M338 70 H755 Q773 70 769 88 L737 215 Q732 232 714 232 H300 C320 200 345 160 345 120 Q345 70 338 70 Z" fill="var(--panel)" stroke="#d2d2d8" stroke-width="1"/>

  <!-- hero photo area -->
  <path class="hero-photo" role="img" aria-label="Photo of a large suburban house with gables, palm trees and a green lawn under a blue sky"
        d="M35 215 C20 150 60 95 110 92 C140 92 165 105 180 120 C185 60 230 30 280 32 C330 35 360 80 345 130 C335 170 300 200 290 240 C280 280 265 310 262 330 C200 300 150 275 110 272 C70 268 45 250 35 215 Z"
        fill="url(#photoTone)" stroke="#ffffff" stroke-width="3"/>

  <!-- main navigation bar -->
  <path class="main-nav-bar" d="M300 241 H710 Q718 241 718 249 V273 Q718 281 710 281 H282 Q284 254 300 241 Z" fill="url(#navRed)"/>

  <!-- quick icon buttons -->
  <g class="quick-buttons" fill="url(#buttonRed)" stroke="#ffffff" stroke-width="1.5">
    <circle cx="122" cy="276" r="22"/>
    <circle cx="172" cy="287" r="22"/>
    <circle cx="220" cy="307" r="22"/>
  </g>
  <g class="quick-icons" fill="none" stroke="#ffffff" stroke-width="1.2">
    <!-- home -->
    <path d="M116 277 L122 271 L128 277 M118 275 V281 H126 V275"/>
    <!-- sitemap -->
    <rect x="170" y="281" width="4" height="3" fill="#ffffff"/>
    <path d="M172 284 V286 M167 288 V286 H177 V288"/>
    <rect x="165" y="288" width="4" height="3" fill="#ffffff"/>
    <rect x="170" y="288" width="4" height="3" fill="#ffffff"/>
    <rect x="175" y="288" width="4" height="3" fill="#ffffff"/>
    <path d="M172 286 V288"/>
    <!-- mail -->
    <rect x="214" y="303" width="12" height="8"/>
    <path d="M214 303 L220 308 L226 303"/>
  </g>

  <!-- search -->
  <rect class="search-field" x="355.5" y="298.5" width="265" height="20" fill="#ffffff" stroke="#b0b0b4"/>
  <path d="M355.5 318.5 V298.5 H620.5" fill="none" stroke="#6e6e72" stroke-width="1.5"/>
  <circle class="search-button" cx="660" cy="310" r="17" fill="url(#buttonRed)" stroke="#ffffff" stroke-width="1.5"/>

  <!-- content panel -->
  <rect class="content-panel" x="267.5" y="336.5" width="448" height="370" rx="4" fill="var(--content)" stroke="var(--border)"/>

  <!-- footer bar -->
  <rect class="footer-bar" x="82" y="721" width="636" height="38" rx="8" fill="url(#footerGrey)"/>
</svg>

<p class="text brand-name">SIAMBAY.Net</p>
<p class="text brand-tagline">The Best Real Estate Company</p>

<nav class="main-nav">
  <a href="#" style="left:502px">HOME</a>
  <a href="#" style="left:597px">PROPERTY</a>
  <a href="#" style="left:745px">RENTALS</a>
  <a href="#" style="left:879px">CONTACTS</a>
</nav>

<p class="text search-label">Search</p>
<p class="text search-go">GO!</p>

<nav class="side-menu">
  <a href="#" style="top:590px">PROPERTY SALES</a>
  <a href="#" style="top:644px">HOILDAY RENTALS</a>
  <a href="#" style="top:698px">LONG TERM RENTALS</a>
  <a href="#" style="top:779px">LOW   END (USD 300K)</a>
  <a href="#" style="top:833px">MID RANGE  (USD 300K -1.5M)</a>
  <a href="#" style="top:887px">HIGH RANGE  (USD 1.5M -8M)</a>
</nav>

<h1 class="text welcome-title">Welcome</h1>

<nav class="footer-nav">
  <a href="#" style="left:210px">HOME</a>
  <a href="#" style="left:396px">PROPERTY</a>
  <a href="#" style="left:615px">RENTALS</a>
  <a href="#" style="left:868px">CONTACTS</a>
</nav>

</body>
</html>
```